Packaging Design Project

We need a bag designed for dried apples. The bag size is 5"W x 7"L. We call the product 'Pear Crumbs'. It is sold in grocery stores and upper end places like Brewtopia etc. The package needs to have a modern look and feel to it and we like the idea of putting a clear window on the front of it so you can see the product. One idea we have is to make the clear window in the shape of an apple. We also like colorful designs but simplicity is important too. Women are the primary buyers and children may ultimately be one of the prime consumers. We anticipate this would be a good product for a child to take to school as a snack. The material would be plastic or some kind of plastic composite. It might be able to work with one color but 2 is also okay. We don't think it needs to be a 4 color job. It is also a resealable bag.

Industry/Entity Type

Plastic

```html
<!DOCTYPE html>
<html lang="en">
<head>
<meta charset="utf-8">
<title>Pear Crumbs – Snack Bag</title>
<link href="https://fonts.googleapis.com/css2?family=Fredoka:wght@600&family=Questrial&display=swap" rel="stylesheet">
<style>
  :root {
    --page: #ffffff;
    --bag-green: #7cb82a;
    --line-green: #b4dc78;
    --window-red: #a51c3c;
    --fruit-light: #f6f0cc;
    --fruit-deep: #d8cc8e;
    --ink-white: #ffffff;
  }
  html, body {
    margin: 0;
    width: 1200px;
    height: 900px;
    overflow: hidden;
    background: var(--page);
    font-family: "Questrial", "Century Gothic", sans-serif;
  }
  .canvas {
    position: relative;
    width: 1200px;
    height: 900px;
  }
  .bag {
    position: absolute;
    left: 314px;
    top: 50px;
    width: 572px;
    height: 800px;
    background: var(--bag-green);
    overflow: hidden;
  }
  .reseal-strip {
    position: absolute;
    left: 0;
    top: 0;
  }
  .reseal-label {
    position: absolute;
    top: 21px;
    left: 0;
    width: 572px;
    text-align: center;
    font-size: 12px;
    letter-spacing: 1.5px;
    color: var(--line-green);
  }
  .reseal-label span {
    background: var(--bag-green);
    padding: 0 10px;
  }
  .product-name {
    position: absolute;
    top: 96px;
    left: 0;
    width: 572px;
    text-align: center;
    margin: 0;
    font-family: "Fredoka", "Arial Rounded MT Bold", sans-serif;
    font-weight: 600;
    font-size: 84px;
    line-height: 1;
    color: var(--window-red);
  }
  .window {
    position: absolute;
    left: 0;
    top: 0;
  }
  .maker {
    position: absolute;
    left: 20px;
    top: 700px;
    display: flex;
    align-items: center;
    gap: 10px;
    color: var(--ink-white);
  }
  .maker-mark {
    width: 52px;
    height: 52px;
    border: 3px solid var(--ink-white);
    border-radius: 50%;
    box-sizing: border-box;
    flex: none;
  }
  .maker-name {
    font-size: 15px;
    line-height: 1.1;
  }
  .maker-web {
    display: block;
    font-size: 10px;
    margin-top: 3px;
  }
  .tagline {
    position: absolute;
    color: var(--ink-white);
    margin: 0;
    line-height: 1;
    white-space: nowrap;
  }
  .tagline-delicious { left: 232px; top: 628px; font-size: 48px; }
  .tagline-healthy   { left: 308px; top: 664px; font-size: 67px; }
  .tagline-snack     { left: 366px; top: 722px; font-size: 50px; }
</style>
</head>
<body>
<main class="canvas">
  <section class="bag" aria-label="Pear Crumbs snack bag front">
    <svg class="reseal-strip" width="572" height="60" viewBox="0 0 572 60" aria-hidden="true">
      <line x1="14" y1="30" x2="558" y2="30" stroke="var(--line-green)" stroke-width="2"/>
      <polyline points="24,24 14,30 24,36" fill="none" stroke="var(--line-green)" stroke-width="2"/>
      <polyline points="548,24 558,30 548,36" fill="none" stroke="var(--line-green)" stroke-width="2"/>
    </svg>
    <div class="reseal-label"><span>REASEALABLE BAG</span></div>

    <h1 class="product-name">Pear Crumbs</h1>

    <svg class="window" width="572" height="800" viewBox="0 0 572 800">
      <defs>
        <linearGradient id="fruitTone" x1="0" y1="0" x2="1" y2="1">
          <stop offset="0" stop-color="var(--fruit-light)"/>
          <stop offset="1" stop-color="var(--fruit-deep)"/>
        </linearGradient>
      </defs>
      <rect role="img" aria-label="Clear window showing the dried fruit pieces inside the bag"
            x="86" y="210" width="420" height="400" rx="60"
            fill="url(#fruitTone)" stroke="var(--window-red)" stroke-width="14"/>
    </svg>

    <div class="maker">
      <div class="maker-mark" aria-hidden="true"></div>
      <div class="maker-name">Little Orchard<span class="maker-web">www.littleorchard.com</span></div>
    </div>

    <p class="tagline tagline-delicious">delicious</p>
    <p class="tagline tagline-healthy">healthy</p>
    <p class="tagline tagline-snack">snack</p>
  </section>
</main>
</body>
</html>
```